Financial Advisor Resource Firm needs business card design

Need business card design for company in Omaha NE called Tallowbrook Partners. We provide resources to financial advisors....workshop programs, retirement analysis, and insurance planning. I would like to see designs that use grays, greens, black, and white colors. The final design should communicate 'collaboration' and be simple yet attractive to financial planning clients. I will attached our logo and another picture of a puzzle piece coming together. I would like the incorporate the puzzle picture somehow, maybe on the back somehow, with color or just the gray scale....OR, the picture be the front of the card with 'Tallowbrook' definition on it (see upload) and then company logo, employee name, title, address on the back (see ppt uploaded). The following disclosure needs to be included somewhere- Advisory services offered through Marlowe Ridge Advisors, LLC.
Updates

I uploaded a svg and ai file of the logo

Target Market(s)

Financial planning clients and financial advisors....so pretty diverse age range of about 40-70.

Industry/Entity Type

Financial Planning

Contact Information for Business Card

Dennis K. Holloway, MBA
Founder/President
5727 E. Larkspur Avenue
Suite 418
Omaha, NE 68297
Phone- (402) 555-0147
Cell- (402) 555-0183
Fax- (402) 555-0129
email- dennis@tallowbrookgroup.example
web address- www.tallowbrookgroup.example

Colors
1b1b1b
474747
d3d3d3
ffffff
9bcb3c
abd036

Requirements
Must have
• Must include logo provided, must be 2 sided, and must have disclosure...all of these items listed in project description

```html
<!DOCTYPE html>
<html lang="en">
<head>
<meta charset="utf-8">
<title>Tallowbrook Partners – Business Card</title>
<link href="https://fonts.googleapis.com/css2?family=Roboto:wght@400;500&display=swap" rel="stylesheet">
<style>
  :root {
    --stage: #f4f4f4;
    --card-dark: #242424;
    --card-light: #ffffff;
    --ink: #1b1b1b;
    --ink-soft: #474747;
    --green: #8cc540;
    --green-deep: #3f6d1f;
    --green-pale: #b9db86;
  }
  * { margin: 0; padding: 0; box-sizing: border-box; }
  html, body { width: 1200px; height: 900px; overflow: hidden; }
  body {
    background: var(--stage);
    font-family: "Roboto", Arial, sans-serif;
    position: relative;
  }
  .card {
    position: absolute;
    width: 597px;
    height: 341px;
    box-shadow: 0 18px 34px rgba(0,0,0,0.28);
  }
  /* Front */
  .card-front {
    left: 302px; top: 97px;
    background: var(--card-dark);
    color: #fff;
    text-align: center;
  }
  .front-name {
    position: absolute;
    left: 0; right: 0; top: 152px;
    font-size: 34px;
    font-weight: 400;
    letter-spacing: 1px;
    color: var(--green);
  }
  .tagline {
    position: absolute;
    left: 0; right: 0; top: 277px;
    font-size: 14px;
  }
  .web {
    position: absolute;
    left: 0; right: 0; top: 301px;
    font-size: 15px;
  }
  .accent { color: var(--green); }

  /* Back */
  .card-back {
    left: 301px; top: 479px;
    background: var(--card-light);
    overflow: hidden;
  }
  .back-art { position: absolute; left: 0; top: 0; }
  .back-name {
    position: absolute;
    left: 47px; top: 198px;
    width: 210px;
    font-size: 21px;
    font-weight: 400;
    color: var(--ink);
    text-align: center;
    line-height: 1.1;
  }
  .person {
    position: absolute;
    left: 312px; top: 110px;
  }
  .person-name {
    font-size: 21px;
    font-weight: 500;
    color: var(--green);
  }
  .person-name .credential {
    font-size: 13px;
    font-weight: 400;
    color: var(--ink);
    margin-left: 4px;
  }
  .person-title {
    font-size: 13.5px;
    color: var(--ink);
    margin-top: 3px;
  }
  .contacts {
    position: absolute;
    left: 312px; top: 172px;
    list-style: none;
  }
  .contacts li {
    display: flex;
    align-items: center;
    height: 24px;
    font-size: 15px;
    color: var(--ink);
  }
  .contacts svg { width: 17px; height: 17px; margin-right: 11px; fill: var(--green); }
  .address {
    position: absolute;
    left: 0; right: 0; top: 299px;
    text-align: center;
    font-size: 15px;
    color: var(--green);
  }
</style>
</head>
<body>

<section class="card card-front">
  <p class="front-name">Tallowbrook Partners</p>
  <p class="tagline">To come <span class="accent">TOGETHER</span> and <span class="accent">UNITE</span> in common interest and <span class="accent">FOCUS</span></p>
  <p class="web">www.<span class="accent">tallowbrookgroup</span>.example</p>
</section>

<section class="card card-back">
  <svg class="back-art" width="597" height="341" viewBox="0 0 597 341">
    <defs>
      <linearGradient id="photoTone" x1="0" y1="0" x2="1" y2="1">
        <stop offset="0" stop-color="#4f8a2a"/>
        <stop offset="0.55" stop-color="#7fb84a"/>
        <stop offset="1" stop-color="#a9d27a"/>
      </linearGradient>
    </defs>
    <path role="img" aria-label="Green-toned photo of hands fitting puzzle pieces together"
          d="M0,0 H597 V40 C520,22 430,32 350,72 C260,118 150,180 0,182 Z"
          fill="url(#photoTone)"/>
    <path d="M336,62 C430,12 530,14 597,52" fill="none" stroke="var(--green)" stroke-width="7"/>
    <path d="M300,86 C420,22 540,20 597,66" fill="none" stroke="var(--green-pale)" stroke-width="2"/>
  </svg>

  <p class="back-name">Tallowbrook Partners</p>

  <div class="person">
    <p class="person-name">Dennis K. Holloway<span class="credential">MBA</span></p>
    <p class="person-title">Founder | President</p>
  </div>

  <ul class="contacts">
    <li>
      <svg viewBox="0 0 24 24"><path d="M6.6 10.8a15 15 0 0 0 6.6 6.6l2.2-2.2a1 1 0 0 1 1-.25 11.4 11.4 0 0 0 3.6.57 1 1 0 0 1 1 1V20a1 1 0 0 1-1 1A17 17 0 0 1 3 4a1 1 0 0 1 1-1h3.5a1 1 0 0 1 1 1c0 1.25.2 2.45.57 3.57a1 1 0 0 1-.25 1z"/></svg>
      (402) 555 - 0147
    </li>
    <li>
      <svg viewBox="0 0 24 24"><path d="M7 1h10a2 2 0 0 1 2 2v18a2 2 0 0 1-2 2H7a2 2 0 0 1-2-2V3a2 2 0 0 1 2-2zm0 3v14h10V4zm5 15.5a1.2 1.2 0 1 0 0 2.4 1.2 1.2 0 0 0 0-2.4z"/></svg>
      (402) 555 - 0183
    </li>
    <li>
      <svg viewBox="0 0 24 24"><path d="M2 7h4v15H2zM8 3h10v5h3a1 1 0 0 1 1 1v12a1 1 0 0 1-1 1H8zm2 2v3h6V5zm0 6v2h2v-2zm4 0v2h2v-2zm4 0v2h2v-2zm-8 4v2h2v-2zm4 0v2h2v-2zm4 0v2h2v-2z"/></svg>
      (402) 555 - 0129
    </li>
    <li>
      <svg viewBox="0 0 24 24"><path d="M2 5h20v14H2zm2 2v.5l8 5 8-5V7l-8 5z"/></svg>
      dennis@tallowbrookgroup.example
    </li>
  </ul>

  <p class="address">5727 E. Larkspur Avenue Suite 418, Omaha, NE 68297</p>
</section>

</body>
</html>
```